Website for peer to peer car sharing service

Hi all,

We need a web design for a new environmental friendly peer-to-peer car sharing website.

The website will serve as a marketplace where car owners can list their car and drivers that who do not have access to a car can rent a suitable car. It is important for us to emphasis that this is a community where the main purpose is to use the vehicles on the street in a more efficient way.

Attached are five pictures where we have sketched up the five main pages:

File 1. Info site for a particular car.
File 2. Logo.
File 3. Register a car.
File 4. Sign up.
File 5. Search.
File 6. Front page.

The logo for the company is attached (File 2) and it would be ideal to design the website in relation to the logo. The final design should relate to a secure market place which is environmental friendly.

We would like this webpage to be in the same spirit as www.velnoro.it, www.brundale.com, www.plimtrovesite.com, https://wend.kul.net, https://garbelow.com etc.

We look forward to see your designs.

Best regards,
The Trundo Team.

Hi guys, 

Please take :

1) Could you please design icons for for  'FAQ' and 'Insurance' in the header, locate the icons right to the Trundo logo. We only want two icons ('FAQ' and 'Insurance')  right to the Trundo logo.

2) The height of the header should be the same as the header of faplex.com

3) The price tags for the cars (below the top section) should be similar to the price tags at mostanbee.com.

4) We would like you to start to design the other pages (the sub-pages listed in the project description:
a)Info site for a particular car.
b)Register a car. 
c)Search results (similar to http://www.pevrotank.com/find-car).

Please take a look at the picture attached for the sub-pages:

https://files.quenmolt.example/brief_uploads/000001_3_search_000001_brief000001.jpg

https://files.quenmolt.example/brief_uploads/000002_4_infositeforaparticularcar_000002_brief000002.jpg

http://www.quenmolt.example/file.aspx?fileLocation=storage_url/brief_uploads/000003_5_registeracar_brief000003.jpg

Best regards, 
Trundo team 

Target Market(s)

The target market are people from 20-40 years old who are environmental friendly, also tourists who visit the city and would like to rent a car.

Industry/Entity Type

It Company

Requirements
Must have
• It is required that the designer that will be chosen will hand in layered PSD files of each web page.

```html
<!DOCTYPE html>
<html lang="en">
<head>
<meta charset="utf-8">
<title>Sign Up – Trundo</title>
<link href="https://fonts.googleapis.com/css2?family=Questrial&family=Open+Sans:wght@400;600;700&family=Ubuntu:wght@400;500;700&display=swap" rel="stylesheet">
<style>
  :root {
    --black: #000000;
    --header-line: #7a7a7a;
    --page-bg: #e6e6e6;
    --card-bg: #ffffff;
    --card-border: #d8d8d8;
    --heading: #3e3e38;
    --link-blue: #3f5c9a;
    --label: #5a5a5a;
    --input-border: #c9c9c9;
    --green: #9bd14a;
    --green-text: #2c3a1a;
    --blue-btn: #4562a0;
    --aside-bg: #f3f3f3;
    --band-bg: #e0e0e0;
    --band-text: #6f6f6f;
    --band-number: #a9a9a9;
    --footer-text: #ffffff;
    --footer-link: #c8c8c8;
    --white: #ffffff;
  }
  * { box-sizing: border-box; margin: 0; padding: 0; }
  html, body { width: 1200px; height: 1016px; overflow: hidden; }
  body {
    position: relative;
    background: var(--page-bg);
    font-family: "Open Sans", Arial, sans-serif;
  }

  /* Header */
  .site-header {
    position: absolute; left: 0; top: 0; width: 1200px; height: 44px;
    background: var(--black); border-bottom: 1px solid var(--header-line);
  }
  .brand {
    position: absolute; left: 98px; top: 9px; display: flex; align-items: center; gap: 6px;
    font-family: "Ubuntu", sans-serif; font-weight: 700; font-size: 21px; color: var(--white);
  }
  .brand-dot { width: 20px; height: 20px; border-radius: 50%; background: var(--green); }
  .header-divider { position: absolute; top: 0; width: 1px; height: 44px; background: #444; }
  .header-icon { position: absolute; top: 8px; }
  .main-nav { position: absolute; top: 0; height: 44px; }
  .main-nav a {
    position: absolute; top: 13px; white-space: nowrap; text-decoration: none;
    font-family: "Ubuntu", sans-serif; font-weight: 500; font-size: 14px; color: var(--white);
  }

  /* Sign up card */
  .signup-card {
    position: absolute; left: 65px; top: 85px; width: 1070px; height: 544px;
    background: var(--card-bg); border: 1px solid var(--card-border);
  }
  .signup-title {
    position: absolute; left: 134px; top: 60px;
    font-family: "Questrial", sans-serif; font-weight: 400; font-size: 45px; color: var(--heading);
  }
  .signup-sub {
    position: absolute; left: 135px; top: 118px;
    font-family: "Questrial", sans-serif; font-size: 22px; color: var(--heading);
  }
  .signup-sub a { color: var(--link-blue); text-decoration: none; }

  .field { position: absolute; left: 0; width: 481px; height: 32px; }
  .field label {
    position: absolute; right: 262px; top: 5px; font-size: 15px; color: var(--label); white-space: nowrap;
  }
  .field input {
    position: absolute; left: 237px; top: 0; width: 243px; height: 32px;
    border: 1px solid var(--input-border); border-radius: 4px; background: var(--white);
  }
  .btn {
    position: absolute; display: flex; align-items: center; justify-content: center;
    font-family: "Ubuntu", sans-serif; font-weight: 700; font-size: 18px; border: 0;
  }
  .btn-signup { left: 242px; top: 409px; width: 130px; height: 43px; background: var(--green); color: var(--green-text); }

  .login-aside {
    position: absolute; left: 567px; top: 212px; width: 294px; height: 178px;
    background: var(--aside-bg); border: 1px solid var(--card-border);
  }
  .login-aside h2 {
    position: absolute; left: 17px; top: 20px;
    font-family: "Questrial", sans-serif; font-weight: 400; font-size: 22px; color: var(--heading);
  }
  .btn-login { left: 17px; top: 63px; width: 120px; height: 43px; background: var(--blue-btn); color: var(--white); }

  /* Help band */
  .help-band {
    position: absolute; left: 0; top: 665px; width: 1200px; height: 111px;
    background: var(--band-bg); border-top: 1px solid #d2d2d2;
  }
  .help-call { position: absolute; right: 608px; top: 20px; text-align: right; }
  .help-call h3 { font-family: "Ubuntu", sans-serif; font-weight: 500; font-size: 22px; color: var(--band-text); }
  .help-call .phone-big {
    font-family: "Ubuntu", sans-serif; font-weight: 700; font-size: 39px; color: var(--band-number); letter-spacing: 1px; line-height: 46px;
  }
  .band-divider { position: absolute; left: 627px; top: 15px; width: 1px; height: 81px; background: #9a9a9a; }
  .connect { position: absolute; left: 660px; top: 20px; }
  .connect h3 { font-family: "Ubuntu", sans-serif; font-weight: 500; font-size: 22px; color: var(--band-text); }
  .social-list { position: absolute; left: -2px; top: 38px; display: flex; gap: 13px; list-style: none; }
  .social-list li { width: 35px; height: 35px; border-radius: 5px; }
  .social-mail { background: linear-gradient(#fafafa, #cfd6dc); border: 1px solid #b9c2ca; }
  .social-a { background: #3b5a9a; }
  .social-b { background: #4fb8de; }
  .social-c { background: #f08a24; }

  /* Footer */
  .site-footer { position: absolute; left: 0; top: 776px; width: 1200px; height: 240px; background: var(--black); color: var(--footer-text); }
  .footer-location { position: absolute; left: 260px; top: 36px; }
  .footer-location h4 { font-family: "Ubuntu", sans-serif; font-weight: 500; font-size: 21px; }
  .footer-location .site-name { font-family: Arial, sans-serif; font-size: 16px; margin-top: 6px; }
  .footer-location address { font-style: normal; font-family: Arial, sans-serif; font-size: 13.5px; line-height: 18px; margin-top: 3px; }
  .footer-contact { position: absolute; left: 520px; top: 76px; font-family: Arial, sans-serif; font-size: 14px; }
  .footer-contact p { display: flex; align-items: center; gap: 8px; height: 28px; }
  .footer-brand {
    position: absolute; left: 816px; top: 70px; display: flex; align-items: center; gap: 8px;
    font-family: "Ubuntu", sans-serif; font-weight: 700; font-size: 38px; color: var(--white);
  }
  .footer-brand .brand-dot { width: 34px; height: 34px; }
  .footer-links { position: absolute; left: 0; top: 182px; width: 1230px; text-align: center; font-family: Arial, sans-serif; font-size: 14px; color: var(--footer-link); }
  .footer-links a { color: var(--footer-link); }
  .copyright { position: absolute; left: 0; top: 203px; width: 1230px; text-align: center; font-family: Arial, sans-serif; font-size: 14px; color: var(--footer-link); }
</style>
</head>
<body>

<header class="site-header">
  <div class="brand"><span class="brand-dot"></span>Trundo</div>
  <span class="header-divider" style="left:216px"></span>
  <svg class="header-icon" style="left:227px" width="20" height="28" viewBox="0 0 20 28" aria-label="FAQ">
    <path d="M3 8 Q3 2 10 2 Q17 2 17 8 Q17 12 12 14 Q10 15 10 19" fill="none" stroke="#fff" stroke-width="4"/>
    <rect x="8" y="22" width="4.5" height="4.5" fill="#fff"/>
  </svg>
  <span class="header-divider" style="left:257px"></span>
  <svg class="header-icon" style="left:268px" width="28" height="28" viewBox="0 0 28 28" aria-label="Insurance">
    <path d="M2 13 Q14 -2 26 13 Q22 11 18 13 Q14 10 10 13 Q6 11 2 13 Z" fill="#fff"/>
    <path d="M14 12 V23 Q14 26 11 26 Q8 26 8 23" fill="none" stroke="#fff" stroke-width="2"/>
  </svg>
  <nav class="main-nav">
    <a href="#" style="left:782px">LIST YOUR CAR</a>
    <a href="#" style="left:946px">LOGIN</a>
    <a href="#" style="left:1033px">SIGN UP</a>
  </nav>
</header>

<main class="signup-card">
  <h1 class="signup-title">Sign UP to Trundo.com</h1>
  <p class="signup-sub">Don’t have an account? <a href="#">Join now!</a></p>

  <form class="signup-form">
    <div class="field" style="top:212px"><label>First Name</label><input type="text"></div>
    <div class="field" style="top:258px"><label>Last Name</label><input type="text"></div>
    <div class="field" style="top:306px"><label>Email</label><input type="email"></div>
    <div class="field" style="top:355px"><label>Password</label><input type="password"></div>
    <button class="btn btn-signup" type="button">SIGN UP</button>
  </form>

  <aside class="login-aside">
    <h2>Already Signed Up?</h2>
    <button class="btn btn-login" type="button">LOGIN</button>
  </aside>
</main>

<section class="help-band">
  <div class="help-call">
    <h3>New Help Planning? Call us!</h3>
    <p class="phone-big">0000 000 0000</p>
  </div>
  <span class="band-divider"></span>
  <div class="connect">
    <h3>Connect with us on</h3>
    <ul class="social-list">
      <li class="social-mail" aria-label="Email"></li>
      <li class="social-a" aria-label="Social network"></li>
      <li class="social-b" aria-label="Social network"></li>
      <li class="social-c" aria-label="Feed"></li>
    </ul>
  </div>
</section>

<footer class="site-footer">
  <div class="footer-location">
    <h4>Location</h4>
    <p class="site-name">trundo.com</p>
    <address>AddressAddressAddressAddress<br>AddressAddressAddressAddress</address>
  </div>
  <div class="footer-contact">
    <p>
      <svg width="26" height="22" viewBox="0 0 26 22" aria-hidden="true"><path d="M3 6 Q3 2 8 2 L18 2 Q23 2 23 6 L23 8 L18 8 L17 5 L9 5 L8 8 L3 8 Z M6 12 L20 12 L22 20 L4 20 Z" fill="#bdbdbd"/></svg>
      (000) 000-0000-(000) 000-0000
    </p>
    <p>
      <svg width="26" height="20" viewBox="0 0 26 20" aria-hidden="true"><rect x="1" y="2" width="24" height="16" fill="#e6e6e6"/><path d="M1 2 L13 11 L25 2" fill="none" stroke="#9a9a9a" stroke-width="1.2"/></svg>
      email@trundo.com
    </p>
  </div>
  <div class="footer-brand"><span class="brand-dot"></span>Trundo</div>
  <p class="footer-links">
    <a href="#">About Us</a> | <a href="#">Privileges</a> | <a href="#">FAQs</a> | <a href="#">Terms</a> | <a href="#">Privacy Policy</a> | <a href="#">Insurance Policy</a> | <a href="#">Press</a> | <a href="#">Contact Us</a> | <a href="#">Mobile Version</a>
  </p>
  <p class="copyright">© 2012 Trundo. All Rights Reserved.</p>
</footer>

</body>
</html>
```